Corporate Travel Technology Company needs new Business Card design

We need a new business card design to reflect our re-branded company. Our company is called vendaXo (pronounced eureka) and we provide Business Intelligence and mobile travel management solutions for the corporate travel industry. Our multinational customers use our solutions to manage large travel budgets and frequent travellers, as well as to save money and reduce risk. We'd like to see designs that use the blue and green palette as well as our corporate logo (attached below). The design should communicate innovation, insight, forward thinking, contemporary, trusted.

Target Market(s)

Large multinational corporates and Travel Agencies.

Industry/Entity Type

Business

Contact Information for Business Card

Marguerite Tallis
Chief Executive
vendaXo
Phone number - +61 (0)2 8147 3092
Email address - marguerite.tallis@vendaxo.example
Mobile number - +61 (0)455 206 718
www.vendaxo.example

Font styles to use
Other font styles liked:
• Please use font as close to corporate logo as possible

Colors
0255a3
0393ce
00a990
33b8a4
33a6d7
3176b5

Requirements
Must have
• Please include the words;
• Mobile Travel Management
• Accelerating Travel Business Insights
• Use corporate logo - although icon can be stylised if needed

```html
<!DOCTYPE html>
<html lang="en">
<head>
<meta charset="utf-8">
<title>vendaXo business card</title>
<link rel="stylesheet" href="https://fonts.googleapis.com/css2?family=Open+Sans:wght@400;600;700&display=swap">
<style>
  :root {
    --page-bg: #e9ecee;
    --card-white: #ffffff;
    --sky-top: #62d2f4;
    --sky-bottom: #1e98d7;
    --slate-light: #5d6e6e;
    --slate-dark: #2b3939;
    --ink: #2f3c3c;
    --wordmark: #4a5a5a;
    --accent-blue: #33a6d7;
    --muted-title: #7d8e94;
    --text-white: #ffffff;
  }
  * { margin: 0; padding: 0; box-sizing: border-box; }
  html, body { width: 1200px; height: 913px; overflow: hidden; }
  body {
    background: var(--page-bg);
    font-family: "Open Sans", Arial, sans-serif;
    position: relative;
  }
  .card {
    position: absolute;
    width: 540px;
    height: 310px;
    border-radius: 18px;
    overflow: hidden;
    box-shadow: 0 10px 28px rgba(0,0,0,0.18);
  }

  /* Front: contact side */
  .card--front {
    left: 70px;
    top: 140px;
    background: linear-gradient(170deg, var(--sky-top), var(--sky-bottom));
  }
  .front-panel {
    position: absolute;
    inset: 0;
    width: 100%;
    height: 100%;
  }
  .contact {
    position: absolute;
    right: 30px;
    top: 34px;
    text-align: right;
    color: var(--text-white);
  }
  .contact__name {
    font-weight: 700;
    font-size: 21px;
    line-height: 1.1;
  }
  .contact__title {
    font-size: 12px;
    color: var(--muted-title);
    margin-bottom: 20px;
  }
  .contact__line {
    display: flex;
    justify-content: flex-end;
    align-items: center;
    gap: 6px;
    font-size: 12.5px;
    line-height: 19px;
  }
  .contact__icon { width: 11px; height: 11px; flex: none; }

  /* Back: brand side */
  .card--back {
    left: 590px;
    top: 463px;
    background: var(--card-white);
  }
  .wordmark {
    position: absolute;
    left: 0;
    right: 0;
    top: 78px;
    text-align: center;
    font-weight: 600;
    font-size: 84px;
    letter-spacing: -1px;
    color: var(--wordmark);
  }
  .taglines {
    position: absolute;
    left: 92px;
    top: 210px;
    list-style: none;
    color: var(--ink);
    font-size: 14px;
    line-height: 19px;
  }
  .taglines li { display: flex; align-items: center; gap: 7px; }
  .taglines li::before {
    content: "";
    width: 8px;
    height: 8px;
    border-radius: 50%;
    background: var(--accent-blue);
  }
</style>
</head>
<body>

  <section class="card card--front" aria-label="Business card front">
    <svg class="front-panel" viewBox="0 0 540 310" preserveAspectRatio="none" aria-hidden="true">
      <defs>
        <linearGradient id="slate" x1="0" y1="0" x2="1" y2="1">
          <stop offset="0" stop-color="var(--slate-light)"/>
          <stop offset="1" stop-color="var(--slate-dark)"/>
        </linearGradient>
      </defs>
      <path d="M0 95 C 80 70, 200 75, 290 130 C 340 165, 330 250, 300 310 L 0 310 Z" fill="url(#slate)"/>
    </svg>

    <div class="contact">
      <p class="contact__name">Marguerite Tallis</p>
      <p class="contact__title">Chief Executive</p>
      <p class="contact__line">+61 (0)455 206 718
        <svg class="contact__icon" viewBox="0 0 12 12" aria-hidden="true"><rect x="3" y="0.5" width="6" height="11" rx="1.2" fill="none" stroke="currentColor"/><circle cx="6" cy="9.5" r="0.7" fill="currentColor"/></svg>
      </p>
      <p class="contact__line">+61 (0)2 8147 3092
        <svg class="contact__icon" viewBox="0 0 12 12" aria-hidden="true"><path d="M2.5 1 L4.5 1 L5.2 3.5 L4 4.6 C4.7 6.2 5.8 7.3 7.4 8 L8.5 6.8 L11 7.5 L11 9.5 C11 10.4 10.3 11 9.5 11 C5 10.6 1.4 7 1 2.5 C1 1.7 1.6 1 2.5 1 Z" fill="currentColor"/></svg>
      </p>
      <p class="contact__line">www.vendaxo.example
        <svg class="contact__icon" viewBox="0 0 12 12" aria-hidden="true"><circle cx="6" cy="6" r="5" fill="none" stroke="currentColor"/><ellipse cx="6" cy="6" rx="2.2" ry="5" fill="none" stroke="currentColor"/><line x1="1" y1="6" x2="11" y2="6" stroke="currentColor"/></svg>
      </p>
      <p class="contact__line">marguerite.tallis@vendaxo.example
        <svg class="contact__icon" viewBox="0 0 12 12" aria-hidden="true"><rect x="0.5" y="2.5" width="11" height="7" fill="none" stroke="currentColor"/><path d="M0.5 2.5 L6 6.5 L11.5 2.5" fill="none" stroke="currentColor"/></svg>
      </p>
    </div>
  </section>

  <section class="card card--back" aria-label="Business card back">
    <p class="wordmark">vendaXo</p>
    <ul class="taglines">
      <li>Mobile Travel Management</li>
      <li>Accelerating Travel Business Insights</li>
    </ul>
  </section>

</body>
</html>
```